Industrial Professional Business Card Design (Vantrel Systems)

Would like professional looking business cards. Not too busy leaning towards minimal. Should have a slogan like:
"Industrial Automation and Control".

We are a tech company that programs industrial PLC computers. We also develop custom hardware solutions. Please use the logo for inspiration.

Target Market(s)

Mining, industrial, processing, automation, factory

Industry/Entity Type

Engineering

Contact Information for Business Card

Name, phone, email, website. job title.

Font styles to use
Other font styles liked:
• droid sans

Requirements
Must have
• Use colours that go well with the logo. Not too busy design.

```html
<!DOCTYPE html>
<html lang="en">
<head>
<meta charset="utf-8">
<title>Vantrel Systems – Business Card</title>
<link rel="stylesheet" href="https://fonts.googleapis.com/css2?family=Open+Sans:wght@400;600&family=Crimson+Text:ital,wght@1,600&display=swap">
<style>
  :root {
    --navy: #1a4a73;
    --orange: #f26a24;
    --paper: #ffffff;
    --ink: #555a60;
    --backdrop: #e9eaec;
  }
  * { margin: 0; padding: 0; box-sizing: border-box; }
  html, body {
    width: 1200px;
    height: 830px;
    overflow: hidden;
    background: var(--backdrop);
    font-family: "Open Sans", sans-serif;
  }
  .card {
    position: absolute;
    left: 100px;
    top: 131px;
    width: 1000px;
    height: 568px;
    background: var(--paper);
    overflow: hidden;
    box-shadow: 0 6px 24px rgba(0, 0, 0, 0.15);
  }
  .card-shapes {
    position: absolute;
    inset: 0;
  }
  .brand {
    position: absolute;
    left: 40px;
    top: 228px;
    width: 380px;
    font-size: 44px;
    font-weight: 400;
    color: var(--navy);
    white-space: nowrap;
    letter-spacing: -0.5px;
  }
  .brand-dot {
    position: absolute;
    left: 196px;
    top: 110px;
    width: 52px;
    height: 52px;
    border-radius: 50%;
    background: var(--orange);
  }
  .person {
    position: absolute;
    right: 45px;
    top: 86px;
    text-align: right;
  }
  .person-name {
    font-size: 31px;
    font-weight: 600;
    color: var(--orange);
    letter-spacing: 1.5px;
    line-height: 40px;
  }
  .person-title {
    font-size: 22px;
    color: var(--paper);
    letter-spacing: 5px;
    line-height: 32px;
  }
  .slogan {
    position: absolute;
    right: 45px;
    top: 190px;
    font-family: "Crimson Text", serif;
    font-style: italic;
    font-weight: 600;
    font-size: 30px;
    color: var(--orange);
  }
  .contact {
    position: absolute;
    font-size: 25px;
    color: var(--ink);
    list-style: none;
  }
  .contact li {
    display: flex;
    align-items: center;
    height: 36px;
  }
  .contact svg { flex: none; }
  .contact-phones { left: 40px; top: 417px; }
  .contact-phones li { gap: 18px; }
  .contact-details { right: 40px; top: 410px; }
  .contact-details li { justify-content: flex-end; gap: 14px; }
  .website {
    position: absolute;
    left: 376px;
    top: 517px;
    font-size: 25px;
    color: var(--orange);
  }
</style>
</head>
<body>
  <div class="card">
    <svg class="card-shapes" width="1000" height="568" viewBox="0 0 1000 568" aria-hidden="true">
      <!-- top band with peak -->
      <path d="M0 0 H1000 V184 H397 L221 4 L50 184 H0 Z" fill="var(--navy)"/>
      <!-- circuit traces -->
      <line x1="490" y1="37" x2="1000" y2="37" stroke="#ffffff" stroke-width="3"/>
      <circle cx="490" cy="37" r="8" fill="var(--orange)" stroke="#ffffff" stroke-width="3"/>
      <line x1="556" y1="64" x2="1000" y2="64" stroke="#ffffff" stroke-width="3"/>
      <circle cx="556" cy="64" r="8" fill="var(--orange)" stroke="#ffffff" stroke-width="3"/>
      <!-- bottom band -->
      <path d="M0 504 H696 L748 568 H0 Z" fill="var(--navy)"/>
      <path d="M696 504 H1000 V568 H748 Z" fill="var(--orange)"/>
      <line x1="0" y1="535" x2="308" y2="535" stroke="#ffffff" stroke-width="3"/>
      <circle cx="308" cy="535" r="8" fill="var(--orange)" stroke="#ffffff" stroke-width="3"/>
    </svg>

    <span class="brand-dot"></span>
    <div class="brand">Vantrel Systems</div>

    <div class="person">
      <div class="person-name">PERSONS NAME</div>
      <div class="person-title">PERSONS TITLE</div>
    </div>

    <div class="slogan">Industrial Automation and Control</div>

    <ul class="contact contact-phones">
      <li>
        <svg width="22" height="22" viewBox="0 0 24 24" aria-hidden="true"><path fill="var(--orange)" d="M6.6 10.8a15.1 15.1 0 0 0 6.6 6.6l2.2-2.2c.3-.3.7-.4 1-.2 1.1.4 2.3.6 3.6.6.6 0 1 .4 1 1V20c0 .6-.4 1-1 1A17 17 0 0 1 3 4c0-.6.4-1 1-1h3.5c.6 0 1 .4 1 1 0 1.3.2 2.5.6 3.6.1.3 0 .7-.2 1Z"/></svg>
        <span>(999) 222-5555</span>
      </li>
      <li>
        <svg width="22" height="22" viewBox="0 0 24 24" aria-hidden="true"><rect x="6" y="2" width="12" height="20" rx="2" fill="none" stroke="var(--orange)" stroke-width="2.4"/><circle cx="12" cy="18" r="1.3" fill="var(--orange)"/></svg>
        <span>(999) 222-4444</span>
      </li>
    </ul>

    <ul class="contact contact-details">
      <li>
        <span>aaaaaa@nnn.com</span>
        <svg width="26" height="20" viewBox="0 0 26 20" aria-hidden="true"><rect x="1" y="2" width="24" height="16" fill="var(--orange)"/><path d="M1 3 L13 12 L25 3" fill="none" stroke="#ffffff" stroke-width="2"/></svg>
      </li>
      <li>
        <span>City, State Name, 77 Street Name</span>
        <svg width="26" height="30" viewBox="0 0 24 30" aria-hidden="true"><path fill="var(--orange)" d="M12 1a10 10 0 0 0-10 10c0 7.5 10 18 10 18s10-10.5 10-18A10 10 0 0 0 12 1Zm0 14a4 4 0 1 1 0-8 4 4 0 0 1 0 8Z"/></svg>
      </li>
    </ul>

    <div class="website">www.sssssssss.com</div>
  </div>
</body>
</html>
```